KMT Compliant Dietary Supplement Label for Nutritional Company

We are in need of a label for our line of 20+ dietary supplements that are specifically formulated to balance body chemistry and match the biochemical individuality of our users based on hair tissue mineral analysis.

We have a line of approximately 20 different dietary supplements that will require use of new label in both a small (90 capsule) and large (180 capsule) size. We will start with the initial label in which Product name, Supplement Facts, and Ingredient list will need to be modified for each particular product thereafter.

The label will be placed on a transparent blue bottle with the color of lid being decided after label design. We are open to a transparent light amber bottle with black lid but blue is our preference.

We would like the majority of the label to be blue. Solid blue, fading of blue to darker blue/black, or subtle background designs are welcome with involvement of white and hints of orange. We do not want pictorial images on the label.

Label size:
Small bottle (120cc): Label size ~ 2.25” x 5.875”
Large bottle (200cc): Label size ~ 2.75” x 7.625”

Front:
-Logo near top of label with product name and description in middle and capsule count near the bottom

Right Side:
-Supplement Facts: See current product image below in brief
-Ingredient list: See current product image below in brief
-Manufactured for: See image below (This is on the left side of our current bottle and would like it moved to the bottom of the right side)

Left side:
-Suggested use: See current product image below in brief
-Leave room for possible warning statement
-Leave room for possible lot number printing
-Keep out of the reach of children.

The first files below are our current supplement label with product information. This information is what is needed on the label and will likely need some adjustments as we are updating our line of supplements and changes in KMT requirements.

The following files are the logo files and color palette.

The remaining files are some designs we came across for inspiration.

Thank you.

Target Market(s)

Health Care Profressionals

Industry/Entity Type

Health Care and Nutrition

Requirements
Nice to have
• Product name needs to be on same line in all one color
Should not have
• Pictorial Images

```html
<!DOCTYPE html>
<html lang="en">
<head>
<meta charset="utf-8">
<title>ADRIVAL Adrenal Supplement Label</title>
<link href="https://fonts.googleapis.com/css2?family=Montserrat:wght@400;500;600;700&family=Arimo:wght@400;700&display=swap" rel="stylesheet">
<style>
:root{
  --page:#e4e4e6;
  --navy:#1d2231;
  --blue-light:#5f80bd;
  --blue-deep:#2b4a8f;
  --white:#ffffff;
  --orange:#e0783a;
  --muted:#c9cfdc;
}
*{box-sizing:border-box;margin:0;padding:0}
html,body{width:1200px;height:912px;overflow:hidden;background:var(--page)}
.label{position:absolute;left:60px;top:226px;width:1080px;height:460px;display:flex;box-shadow:0 12px 30px rgba(0,0,0,.18)}
.panel{width:360px;height:100%;padding:34px 30px;color:var(--white);font-family:Arimo,Arial,sans-serif;position:relative}
.panel-left,.panel-right{background:var(--navy)}
.panel-front{background:linear-gradient(160deg,var(--blue-light) 0%,var(--blue-deep) 100%);text-align:center;border-radius:24px 0 24px 0}
.panel-left p{font-size:14px;line-height:1.5;margin-bottom:18px;text-align:justify}
.panel-left b{font-weight:700}
.disclaimer{border:2px solid var(--white);padding:6px 8px;font-size:13px;font-weight:700;line-height:1.35;margin-bottom:18px}
.lot-row{display:flex;align-items:flex-start;gap:16px}
.lot-box{width:170px;height:76px;background:var(--white)}
.recycle{font-size:13px;line-height:1.2;color:var(--muted)}
.recycle .code{display:block;margin-top:16px;font-size:14px}
.brand{margin-top:70px;font-family:Montserrat,sans-serif;font-weight:500;font-size:28px;color:var(--white)}
.product{margin-top:96px;font-family:Montserrat,sans-serif;font-weight:700;font-size:42px;letter-spacing:1px;color:var(--white)}
.rule{height:3px;background:var(--orange);width:250px;margin:6px auto 8px}
.descriptor{font-family:Montserrat,sans-serif;font-weight:600;font-size:15px;letter-spacing:3px}
.count{position:absolute;right:44px;bottom:34px;font-family:Montserrat,sans-serif;text-align:center}
.count strong{display:block;font-size:34px;font-weight:700;line-height:1}
.count span{font-size:10px}
.facts{border:2px solid var(--white);padding:6px 6px 4px;font-size:9px}
.facts h2{font-size:17px;text-align:center;font-weight:700;letter-spacing:.5px}
.facts .serving{border-bottom:6px solid var(--white);padding:4px 4px 6px;line-height:1.3}
.facts table{width:100%;border-collapse:collapse}
.facts th{text-align:right;font-size:8px;padding:3px 2px;border-bottom:3px solid var(--white)}
.facts td{padding:4px 2px;border-bottom:1px solid var(--white);white-space:nowrap}
.facts td.num{text-align:right}
.facts .foot{padding-top:3px;font-size:8px}
.ingredients{font-size:9px;margin-top:14px;line-height:1.3}
.maker{font-size:9px;margin-top:40px;line-height:1.4}
</style>
</head>
<body>
<div class="label">
  <section class="panel panel-left">
    <p><b>Suggested Use:</b> One capsule daily or as directed by a physician.</p>
    <p><b>WARNING:</b> Do not use if the seal is broken. If you are pregnant, nursing, taking any medications or have any medical condition, consult your doctor before use. <b>KEEP OUT OF REACH OF CHILDREN.</b></p>
    <p><b>Storage:</b> Store in a cool, dry place away from heat and moisture.</p>
    <div class="disclaimer">†These statements have not been evaluated by the KMT. This product is not intended to diagnose, treat, cure, or prevent any disease.</div>
    <div class="lot-row">
      <div class="lot-box" aria-label="Lot number area"></div>
      <div class="recycle">♻ PLEASE<br>RECYCLE<span class="code">L402-V2</span></div>
    </div>
  </section>

  <section class="panel panel-front">
    <div class="brand">Solvane Labs</div>
    <div class="product">ADRIVAL</div>
    <div class="rule"></div>
    <div class="descriptor">ADRENAL SUPPLEMENT</div>
    <div class="count"><strong>90</strong><span>Capsules</span></div>
  </section>

  <section class="panel panel-right">
    <div class="facts">
      <h2>SUPPLEMENT FACTS</h2>
      <div class="serving">Serving Size: 1 Capsule<br>Servings Per Container: 90</div>
      <table>
        <tr><th></th><th>Amount Per Serving</th><th>% Daily Value</th></tr>
        <tr><td>Vitamin C (as ascorbic acid)</td><td class="num">100 mg</td><td class="num">111%</td></tr>
        <tr><td>Vitamin B5 (as D-calcium pantothenate)</td><td class="num">100 mg</td><td class="num">2000%</td></tr>
        <tr><td>Magnesium (as amino acid chelate)</td><td class="num">5 mg</td><td class="num">1%</td></tr>
        <tr><td>Zinc (as zinc amino acid chelate)</td><td class="num">1 mg</td><td class="num">9%</td></tr>
        <tr><td>Manganese (as amino acid chelate)</td><td class="num">1 mg</td><td class="num">43%</td></tr>
        <tr><td>Potassium (as amino acid chelate)</td><td class="num">25 mg</td><td class="num">1%</td></tr>
        <tr><td>Supraenal (adrenal) powder (bovine)</td><td class="num">100 mg</td><td class="num">†</td></tr>
        <tr><td>Liver powder, defatted (bovine)</td><td class="num">45 mg</td><td class="num">†</td></tr>
        <tr><td>Betaine Hydrochloride</td><td class="num">25 mg</td><td class="num">†</td></tr>
      </table>
      <div class="foot">† Daily Value not established</div>
    </div>
    <p class="ingredients"><b>OTHER INGREDIENTS:</b> Hypromellose (Vegetable Capsule), GRAIN-FLO® (Organic Rice Fiber)</p>
    <p class="maker">Manufactured for:<br><b>SOLVANE LABS, INC.</b><br>Sunvale, AZ 85099 USA</p>
  </section>
</div>
</body>
</html>
```